MR Business Card

I want to create a simple business card.
I am a consultant. I design and develop furniture, lighting and accessories for hospitality and retail brands.
I want the card to be simple and clean. Not too much of a logo - but it needs the basic information shown on the attached file.
Also - I have shown some fonts that I like on the attached file.
The card can be square or rectangle. It should be double sided.
I prefer 1-2 colors (not too colorful - but using color an an accent) Even if using color on the edges as an accent.

My snapgrove link shows some other graphics styles that I like. I like clean and simple.
http://www.snapgrove-boards.net/marenrosko/business-cards/

```html
<!DOCTYPE html>
<html lang="en">
<head>
<meta charset="utf-8">
<title>MR Business Card</title>
<link rel="stylesheet" href="https://fonts.googleapis.com/css2?family=Arimo:wght@400;700&display=swap">
<style>
  :root {
    --backdrop: #9aa3a4;
    --card: #ffffff;
    --stone: #a6b2b1;
    --accent: #2f8db0;
  }
  * { margin: 0; padding: 0; box-sizing: border-box; }
  html, body {
    width: 1200px;
    height: 1000px;
    overflow: hidden;
  }
  body {
    position: relative;
    background: var(--backdrop);
    font-family: "Arimo", Arial, sans-serif;
  }
  .card {
    position: absolute;
    left: 162px;
    width: 836px;
    background: var(--card);
  }
  .card--front { top: 103px; height: 386px; }
  .card--back  { top: 521px; height: 383px; }

  .name {
    position: absolute;
    left: 41px;
    top: 250px;
    color: var(--stone);
    font-weight: 700;
    font-size: 60px;
    line-height: 46px;
    letter-spacing: -1.5px;
  }
  .name__last { display: block; padding-left: 44px; }

  .contact {
    position: absolute;
    left: 365px;
    top: 298px;
    color: var(--stone);
    font-size: 23px;
    line-height: 26px;
    letter-spacing: -0.3px;
  }
  .contact__phone { font-weight: 700; }

  .tagline {
    position: absolute;
    left: 43px;
    top: 287px;
    color: var(--stone);
    font-size: 29px;
    font-weight: 700;
    letter-spacing: -0.8px;
  }
  .tagline__amp {
    color: var(--accent);
    text-decoration: underline;
    text-decoration-thickness: 3px;
    text-underline-offset: 3px;
    font-size: 22px;
  }
  .services {
    position: absolute;
    left: 45px;
    top: 323px;
    font-size: 23px;
    font-weight: 700;
    letter-spacing: -0.2px;
    white-space: nowrap;
  }
  .services__item--muted { color: var(--stone); }
  .services__item--accent { color: var(--accent); }
  .services__sep { font-weight: 400; margin: 0 6px; }
  .services__sep--muted { color: var(--stone); }
  .services__sep--accent { color: var(--accent); }
</style>
</head>
<body>
  <section class="card card--front" aria-label="Card front">
    <h1 class="name">MAREN<span class="name__last">ROSKO</span></h1>
    <p class="contact">
      <span class="contact__email">maren@marenrosko.com</span><br>
      <span class="contact__phone">917.555.0142</span>
    </p>
  </section>

  <section class="card card--back" aria-label="Card back">
    <p class="tagline">design<span class="tagline__amp">&amp;</span>development</p>
    <p class="services">
      <span class="services__item--muted">hospitality</span><span class="services__sep services__sep--muted">|</span><span class="services__item--muted">home</span><span class="services__sep services__sep--accent">|</span><span class="services__item--accent">furniture</span><span class="services__sep services__sep--accent">|</span><span class="services__item--accent">fixtures</span><span class="services__sep services__sep--accent">|</span><span class="services__item--accent">lighting</span><span class="services__sep services__sep--accent">|</span><span class="services__item--accent">textiles</span><span class="services__sep services__sep--accent">|</span><span class="services__item--accent">etc</span>
    </p>
  </section>
</body>
</html>
```